Business Card Design

Copperfield Lantern & Spark, Inc. (CLS), located in Memphis, TN began operating on 2003. We are a certified
minority woman-owned business that genuinely takes a vested interest in our customers. We serve utilities,
government, contractors and end user markets in electrical, water, gas and industrial supplies. Our core
competency as a distributor of electrical materials has positioned us to serve business of all size. As your supply
chain partner, we arm you with the resources you need to make your supply chain more efficient. Our team
works with your team on a daily basis to help you solve problems and achieve goals. This team approach has
helped CLS customers to succeed and we can do the same for you.

NAICS Codes:
423610 Electrical Apparatus and Equipment, Wiring Supplies, and Related Equipment Merchant
Wholesalers
423510 Metal Service Centers and Other Metal Merchant Wholesalers
423720 Plumbing and Heating Equipment and Supplies (Hydronics) Merchant Wholesalers

Certifications
MBE (KRVPQAL, State of Tennessee Up-MRX and FJW), WBE (HQOLT),
WOSB, DOT (TDOT, MDOT, ALDOT, SCDOT, NCDOT, and VDOT), LOSB,
SBE, and LSB Certified
Some of Our Products Include:
. Boxes & Covers
. Conduit & Raceway
. Fittings
. Fuses
. Lamp & Ballasts
. Lighting Controls & Timers
. Lighting Fixtures
. Personal Safety
. Pipes
. Power Distribution
. Terminations Ground & Splices
. Tools & Testers
. Wire, Cords & Cable
. Wiring Devices
. Valves

Industry/Entity Type

Business

Contact Information for Business Card

Marianne T. Holloway - President/CEO
4728 Quillon Ave., Memphis, TN 38127
901-555-0147 office, 901-555-0182 fax, 901-555-0163 cell
mtholloway@clsllc-example.com - www.clsincorp-example.com

```html
<!DOCTYPE html>
<html lang="en">
<head>
<meta charset="utf-8">
<title>Copperfield Lantern &amp; Spark – Business Card</title>
<link href="https://fonts.googleapis.com/css2?family=Cinzel:wght@600&family=Gelasio:wght@400;700&family=Arimo:wght@400&display=swap" rel="stylesheet">
<style>
  :root {
    --backdrop: #e8e6e3;
    --white: #ffffff;
    --ink: #000000;
    --olive-band: #b1ae3a;
    --olive-back: #b1ad03;
  }
  * { margin: 0; padding: 0; box-sizing: border-box; }
  html, body { width: 1189px; height: 1200px; overflow: hidden; background: var(--backdrop); }
  .canvas { position: relative; width: 1189px; height: 1200px; }

  .card {
    position: absolute; left: 140px; width: 918px; height: 524px; overflow: hidden;
    box-shadow: 0 3px 8px rgba(0,0,0,.25);
  }
  .card-front { top: 45px; background: var(--white); }
  .card-back { top: 623px; background: var(--olive-back); }

  .wordmark-line {
    position: absolute; white-space: nowrap; color: var(--ink);
    font-family: "Cinzel", serif; font-weight: 600; line-height: 1;
  }
  .card-front .wordmark-top { left: 165px; top: 100px; font-size: 53px; }
  .card-front .wordmark-bottom { left: 290px; top: 152px; font-size: 46px; }
  .card-back .wordmark-top { left: 31px; top: 205px; font-size: 74px; }
  .card-back .wordmark-bottom { left: 240px; top: 282px; font-size: 62px; }

  .wave { position: absolute; left: 0; top: 0; width: 918px; height: 524px; }
  .wave .band { fill: var(--olive-band); }
  .wave .field { fill: var(--ink); }

  .holder { position: absolute; left: 25px; top: 366px; width: 375px; color: var(--white); }
  .holder-name { font-family: "Gelasio", serif; font-weight: 700; font-size: 32px; line-height: 1.1; white-space: nowrap; }
  .holder-title { font-family: "Arimo", sans-serif; font-size: 22px; line-height: 1; margin-top: 3px; }

  .divider { position: absolute; left: 411px; top: 302px; width: 2px; height: 198px; background: var(--white); }

  .contacts { position: absolute; left: 423px; top: 300px; list-style: none; color: var(--white); }
  .contacts li { display: flex; align-items: center; height: 35.6px; white-space: nowrap; }
  .contacts .icon { width: 21px; height: 21px; margin-right: 14px; flex: none; }
  .contacts .icon rect.tile { fill: var(--white); }
  .contacts .icon .glyph { fill: var(--ink); }
  .contacts .sans { font-family: "Arimo", sans-serif; font-size: 21px; }
  .contacts .serif { font-family: "Gelasio", serif; font-size: 21px; }
</style>
</head>
<body>
<main class="canvas">

  <section class="card card-front" aria-label="Business card front">
    <div class="wordmark-line wordmark-top">COPPERFIELD</div>
    <div class="wordmark-line wordmark-bottom">LANTERN &amp; SPARK</div>

    <svg class="wave" viewBox="0 0 918 524" aria-hidden="true">
      <path class="band" d="M0 241 C200 292 480 205 700 220 C800 227 870 250 918 270 V524 H0 Z"/>
      <path class="field" d="M0 294 C240 340 500 240 720 246 C820 249 880 268 918 286 V524 H0 Z"/>
    </svg>

    <div class="holder">
      <div class="holder-name">Marianne T. Holloway</div>
      <div class="holder-title">President/CEO</div>
    </div>

    <div class="divider"></div>

    <ul class="contacts">
      <li>
        <svg class="icon" viewBox="0 0 21 21" aria-label="Office"><rect class="tile" width="21" height="21"/><path class="glyph" d="M4 9 Q10.5 3 17 9 L15 11 L13 9.5 V8 H8 V9.5 L6 11 Z M6 12 H15 V16 H6 Z"/></svg>
        <span class="sans">901-555-0147</span>
      </li>
      <li>
        <svg class="icon" viewBox="0 0 21 21" aria-label="Cell"><rect class="tile" width="21" height="21"/><path class="glyph" d="M6 3 L9 3 L10 7 L8 8.5 Q9 12 12.5 14 L14 12 L18 13 L18 16 Q16 18 13 17 Q6 14 4 7 Q4 4 6 3 Z"/></svg>
        <span class="sans">901-555-0163</span>
      </li>
      <li>
        <svg class="icon" viewBox="0 0 21 21" aria-label="Fax"><rect class="tile" width="21" height="21"/><path class="glyph" d="M6 3 H15 V8 H6 Z M3 9 H18 V15 H15 V18 H6 V15 H3 Z"/></svg>
        <span class="sans">901-555-0182</span>
      </li>
      <li>
        <svg class="icon" viewBox="0 0 21 21" aria-label="Email"><rect class="tile" width="21" height="21"/><path class="glyph" d="M3 5 H18 V16 H3 Z M4.5 6.5 L10.5 11 L16.5 6.5 V7.8 L10.5 12.3 L4.5 7.8 Z" fill-rule="evenodd"/></svg>
        <span class="serif">mtholloway@clsllc-example.com</span>
      </li>
      <li>
        <svg class="icon" viewBox="0 0 21 21" aria-label="Website"><rect class="tile" width="21" height="21"/><circle class="glyph" cx="10.5" cy="10.5" r="7"/><path d="M6 9 Q9 6 10 9 Q12 12 9 15 M12 5 Q15 8 17 9" stroke="#fff" stroke-width="1.5" fill="none"/></svg>
        <span class="serif">www.clsincorp-example.com</span>
      </li>
      <li>
        <svg class="icon" viewBox="0 0 21 21" aria-label="Address"><rect class="tile" width="21" height="21"/><path class="glyph" d="M10.5 3 A5 5 0 0 1 15.5 8 Q15.5 12 10.5 18 Q5.5 12 5.5 8 A5 5 0 0 1 10.5 3 Z"/><circle cx="10.5" cy="8" r="1.8" fill="#fff"/></svg>
        <span class="serif">4728 Quillon Ave., Memphis, TN 38127</span>
      </li>
    </ul>
  </section>

  <section class="card card-back" aria-label="Business card back">
    <div class="wordmark-line wordmark-top">COPPERFIELD</div>
    <div class="wordmark-line wordmark-bottom">LANTERN &amp; SPARK</div>
  </section>

</main>
</body>
</html>
```